Banner ad series

We need a series of banner ads for 4 different digital products. The ads will drive traffic to these landing pages:
Relocate.set: http://quillfernwares.example/relocateset/
Treasures.rec: http://quillfernwares.example/digital-treasures-rec/
Jumpstep Drill Week: http://quillfernwares.example/jumpstep-drill-week/
Vital Habits Drill Week: http://quillfernwares.example/vital-habits/

Banner Ad Sizes needed:
160x600, 728x90, 300x250

Text files with the copy/variations needed for each product are attached. In the text file - the first line of each option is the main headline. All other copy is support copy and OPTIONAL.

Target Market(s)

Our target market is a woman between the ages of 30-55 with kids. She's smart, working professionally and always on the lookout for products and services that will help her get more organized.

Industry/Entity Type

Digital

Requirements
Must have
• Quillfern logo

```html
<!DOCTYPE html>
<html lang="en">
<head>
<meta charset="utf-8">
<title>Quillfern Relocate.set Banner Series</title>
<link rel="stylesheet" href="https://fonts.googleapis.com/css2?family=Noto+Serif:wght@400;700&family=Open+Sans:wght@400;700&display=swap">
<style>
  :root {
    --teal-deep: #578c85;
    --teal: #6aa39b;
    --teal-light: #79b0a8;
    --grid-tone: #b7cfc9;
    --pink: #d8184e;
    --pink-dark: #b80f3f;
    --white: #ffffff;
    --ink-soft: #5b5b5b;
    --serif: "Noto Serif", Georgia, serif;
    --sans: "Open Sans", Arial, sans-serif;
  }
  * { box-sizing: border-box; margin: 0; padding: 0; }
  html, body { width: 1200px; height: 900px; overflow: hidden; background: var(--white); }
  body { position: relative; font-family: var(--serif); }

  .banner { position: absolute; overflow: hidden; background: var(--teal-deep); color: var(--white); }
  .banner--wide { left: 150px; top: 48px; width: 900px; height: 239px; }
  .banner--leader { left: 54px; top: 313px; width: 1092px; height: 135px; }
  .banner--square { left: 375px; top: 475px; width: 450px; height: 375px; }

  .banner__backdrop { position: absolute; inset: 0; width: 100%; height: 100%; }
  .grid-area { fill: var(--grid-tone); }
  .panel { fill: url(#panelShade); filter: drop-shadow(0 3px 4px rgba(0,0,0,.3)); }

  .headline { position: absolute; font-family: var(--serif); font-weight: 700; line-height: 1; white-space: nowrap;
    text-shadow: 1px 2px 3px rgba(0,0,0,.25); }
  .moving { display: inline-block; white-space: nowrap; }
  .moving span { display: inline-block; }
  .moving .m { font-size: 1.25em; transform: rotate(-4deg); }
  .moving .o { font-size: .8em; transform: translateY(.18em) rotate(8deg); }
  .moving .v { font-size: 1em; transform: translateY(.12em) rotate(-6deg); }
  .moving .i { font-size: .95em; transform: rotate(5deg); }
  .moving .n { font-size: .95em; transform: translateY(.06em) rotate(-3deg); }
  .moving .g { font-size: 1em; transform: rotate(4deg); }
  .qmark { display: inline-block; font-size: 1.35em; margin-left: .08em; }

  .tick { position: absolute; width: 42px; height: 42px; }
  .support { position: absolute; font-size: 28px; line-height: 39px; font-weight: 400; white-space: nowrap; }
  .support strong { font-weight: 700; }

  .logo-card { position: absolute; background: var(--white); border-radius: 9px; box-shadow: 0 2px 5px rgba(0,0,0,.35);
    padding: 5px; }
  .logo-card__inner { width: 100%; height: 100%; border: 2px dotted var(--ink-soft); border-radius: 6px;
    display: flex; align-items: flex-end; justify-content: flex-end; padding: 0 12px 14px; gap: 8px; }
  .logo-card__name { font-family: var(--serif); font-weight: 400; color: var(--pink); line-height: 1; }
  .logo-card__dot { width: 12px; height: 12px; border-radius: 50%; background: var(--pink); flex: none; }

  .cta { position: absolute; display: flex; align-items: center; justify-content: center; border-radius: 9px;
    background: linear-gradient(var(--pink), var(--pink-dark)); color: var(--white); font-family: var(--sans);
    font-size: 16px; white-space: nowrap; text-decoration: none; box-shadow: 0 2px 3px rgba(0,0,0,.3); }
  .cta strong { margin-left: .3em; font-weight: 700; }
</style>
</head>
<body>

<svg width="0" height="0" style="position:absolute">
  <defs>
    <linearGradient id="panelShade" x1="0" y1="0" x2="0" y2="1">
      <stop offset="0" stop-color="#72aaa2"/>
      <stop offset="1" stop-color="#5f968f"/>
    </linearGradient>
    <symbol id="tickMark" viewBox="0 0 42 42">
      <circle cx="21" cy="21" r="20" fill="#d8184e"/>
      <path d="M11 21.5 L18 28.5 L31 14" fill="none" stroke="#ffffff" stroke-width="5" stroke-linecap="round" stroke-linejoin="round"/>
    </symbol>
  </defs>
</svg>

<!-- 900 x 239 -->
<a class="banner banner--wide" href="http://quillfernwares.example/relocateset/">
  <svg class="banner__backdrop" viewBox="0 0 900 239" preserveAspectRatio="none">
    <rect class="grid-area" x="8" y="110" width="300" height="129" role="img" aria-label="Pale tiled grid texture"/>
    <path class="panel" d="M0 0 H900 V239 H330 C300 239 300 205 280 190 C260 175 220 170 180 166 L0 160 Z"/>
  </svg>
  <div class="headline" style="left:68px; top:26px; font-size:54px;">Need help <span class="moving"><span class="m">M</span><span class="o">O</span><span class="v">V</span><span class="i">I</span><span class="n">N</span><span class="g">G</span></span><span class="qmark">?</span></div>
  <svg class="tick" style="left:139px; top:118px;"><use href="#tickMark"/></svg>
  <p class="support" style="left:200px; top:120px;">This digital tool is your key<br>to a <strong>stress-free</strong> move</p>
  <div class="logo-card" style="left:680px; top:18px; width:210px; height:157px;">
    <div class="logo-card__inner"><span class="logo-card__dot"></span><span class="logo-card__name" style="font-size:30px;">quillfern</span></div>
  </div>
  <span class="cta" style="left:687px; top:196px; width:187px; height:35px;">Click here to<strong>learn more</strong></span>
</a>

<!-- 1092 x 135 -->
<a class="banner banner--leader" href="http://quillfernwares.example/relocateset/">
  <svg class="banner__backdrop" viewBox="0 0 1092 135" preserveAspectRatio="none">
    <rect class="grid-area" x="900" y="0" width="192" height="135" role="img" aria-label="Pale tiled grid texture"/>
    <path class="panel" d="M0 0 H900 C930 20 935 50 942 70 L948 135 H0 Z"/>
  </svg>
  <div class="headline" style="left:33px; top:14px; font-size:51px;">Need help</div>
  <div class="headline" style="left:50px; top:64px; font-size:46px;"><span class="moving"><span class="m">M</span><span class="o">O</span><span class="v">V</span><span class="i">I</span><span class="n">N</span><span class="g">G</span></span><span class="qmark">?</span></div>
  <svg class="tick" style="left:327px; top:23px;"><use href="#tickMark"/></svg>
  <p class="support" style="left:380px; top:22px;">This digital tool is your key<br>to a <strong>stress-free</strong> move</p>
  <span class="cta" style="left:726px; top:86px; width:184px; height:33px;">Click here to<strong>learn more</strong></span>
  <div class="logo-card" style="left:940px; top:12px; width:142px; height:102px;">
    <div class="logo-card__inner" style="padding:0 8px 10px; gap:6px;"><span class="logo-card__dot" style="width:9px;height:9px;"></span><span class="logo-card__name" style="font-size:20px;">quillfern</span></div>
  </div>
</a>

<!-- 450 x 375 -->
<a class="banner banner--square" href="http://quillfernwares.example/relocateset/">
  <svg class="banner__backdrop" viewBox="0 0 450 375" preserveAspectRatio="none">
    <rect class="grid-area" x="297" y="250" width="153" height="125" role="img" aria-label="Pale tiled grid texture"/>
    <path class="panel" d="M0 0 H450 V150 C450 200 445 240 425 262 C400 270 340 268 300 275 L296 375 H0 Z"/>
  </svg>
  <div class="headline" style="left:72px; top:24px; font-size:54px;">Need help</div>
  <div class="headline" style="left:90px; top:80px; font-size:50px;"><span class="moving"><span class="m">M</span><span class="o">O</span><span class="v">V</span><span class="i">I</span><span class="n">N</span><span class="g">G</span></span><span class="qmark">?</span></div>
  <svg class="tick" style="left:21px; top:151px;"><use href="#tickMark"/></svg>
  <p class="support" style="left:78px; top:155px;">This digital tool is your<br>key to a <strong>stress-free</strong> move</p>
  <div class="logo-card" style="left:82px; top:247px; width:149px; height:110px;">
    <div class="logo-card__inner" style="padding:0 8px 10px; gap:6px;"><span class="logo-card__dot" style="width:9px;height:9px;"></span><span class="logo-card__name" style="font-size:21px;">quillfern</span></div>
  </div>
  <span class="cta" style="left:253px; top:295px; width:184px; height:32px;">Click here to<strong>learn more</strong></span>
</a>

</body>
</html>
```